Website redesign for fast growing company looking to present a unique image

We're looking to revamp our online image to represent the professional, accomplished company we have become. We want to move beyond a templated look and feel to a custom design - we are eager to have you design a new public face for us! In particular, we need creative ways to display text to stand out. We are reaching top-level, C-suite executives and want to give them the confidence that we have the skills, talent, expertise, and knowledge to help their companies grow.
Updates

Designs look the same

Target Market(s)

contact centers, business process outsourcing

Industry/Entity Type

Call Center

Coding

Coded - Design and coding required

Number of Pages Required

4 page

Font styles to use
Sans Serif

Colors

Designer to choose colors to be used in the design.

Requirements
Must have
• Designed for a professional audience - C-suite executives - but that also shows our personality as a company that is nimble, personable, trustworthy, and smart. Must be lively, but not quirky. Professional, but not overly formal. Be bold with choices for imagery - we want to look unique so go beyond traditional "business/corporate" stock photos. Instead use imagery similar to what is on our staging website - torvenda.com/staging. Do not use the "neon" sign. Use colors to match and complement our logo - bright orange and dark blue. Creative text boxes that we can use throughout the site. I have attached pages of our current staging site to display some of the types of imagery that might work. We are looking for "professional with a personality" Note: this design will be transferred into a Wordpress framework.
Nice to have
• We like the animated text features of the Vorquin.com site - bold colors, great display of text features that break up the page and engage people to continue scrolling.
Should not have
• Cheesy stock photos of call center agents wearing headsets. Overly used stock photos of professionals in suits shaking hands, high-rise buildings, connection/network graphics. Current management does not like the neon sign graphics displayed on our staging site (torvenda.com/staging). We do not like style of sites that use cartoon-like icons and figures.

```html
<!DOCTYPE html>
<html lang="en">
<head>
<meta charset="utf-8">
<title>Torvenda — Contact Center Experts</title>
<link href="https://fonts.googleapis.com/css2?family=Catamaran:wght@600;700;800&family=Roboto:wght@400;500;700&display=swap" rel="stylesheet">
<style>
:root{
  --orange:#f15a29;
  --orange-soft:#f26a3a;
  --navy:#1f4a78;
  --navy-deep:#173a60;
  --blue:#2d6aa8;
  --ink:#1d1d1f;
  --grey:#777;
  --line:#c9c9c9;
  --white:#fff;
}
*{box-sizing:border-box;margin:0;padding:0}
html,body{width:1200px;height:4277px;overflow:hidden}
body{font-family:'Roboto',sans-serif;color:var(--ink);background:var(--white);position:relative}
h1,h2,h3{font-family:'Catamaran',sans-serif}
section,header,footer{position:absolute;left:0;width:1200px}

/* nav */
.site-nav{top:0;height:80px;background:var(--navy);z-index:5}
.brand{position:absolute;left:143px;top:18px;display:flex;align-items:center;gap:10px;color:var(--orange);font-family:'Catamaran',sans-serif;font-weight:700;font-size:40px;line-height:44px}
.brand-mark{width:14px;height:14px;border-radius:50%;background:var(--orange)}
.menu{position:absolute;left:494px;top:31px;display:flex;gap:26px;font-size:12px;font-weight:700;color:var(--white);list-style:none}
.menu li.active{border-bottom:3px solid var(--orange);padding-bottom:6px}
.search{position:absolute;left:1021px;top:22px;width:35px;height:35px;border-radius:50%;background:var(--orange)}

/* hero */
.hero{top:0;height:800px;overflow:hidden}
.hero-photo{position:absolute;inset:0;background:linear-gradient(120deg,#253447 0%,#3b4c60 45%,#6b7b8d 70%,#2a3a4d 100%)}
.hero-copy{position:absolute;left:143px;top:240px;color:var(--white)}
.hero-copy h1{font-size:44px;font-weight:700;line-height:56px;letter-spacing:-.5px}
.hero-copy p{font-size:22px;font-weight:500;line-height:32px;margin-top:22px}
.btn{display:inline-flex;align-items:center;gap:10px;background:var(--orange);color:var(--white);font-weight:500;border-radius:30px}
.hero .btn{margin-top:44px;height:57px;padding:0 36px;font-size:18px}
.dots{position:absolute;left:1128px;top:358px;display:flex;flex-direction:column;gap:11px}
.dots span{width:9px;height:9px;border-radius:50%;background:var(--white)}
.dots span.on{background:var(--orange)}
.hero-cut{position:absolute;left:0;bottom:0}

/* intro */
.intro{top:800px;height:265px;text-align:center;background:linear-gradient(180deg,#fff 0%,#f4f5f7 100%)}
.intro h2{font-size:38px;font-weight:700;margin-top:72px}
.intro p{font-size:14px;color:var(--grey);line-height:32px;margin-top:14px}

/* strengths */
.strengths{top:1065px;height:755px;text-align:center;color:var(--white)}
.strengths-photo{position:absolute;inset:0;background:linear-gradient(180deg,#2d6aa8 0%,#2a5f98 55%,#244f80 100%)}
.strengths h2{position:relative;font-size:38px;font-weight:700;margin-top:170px}
.strengths .lede{position:relative;font-size:20px;margin-top:18px}
.pillars{position:absolute;left:143px;top:352px;display:flex;gap:40px;list-style:none}
.pillars li{width:150px;font-size:17px;font-weight:700;line-height:24px}
.ring{width:150px;height:150px;border-radius:50%;border:4px solid var(--orange);display:flex;align-items:center;justify-content:center;margin-bottom:22px}
.ring-inner{width:132px;height:132px;border-radius:50%;border:3px solid var(--white);display:flex;align-items:center;justify-content:center}
.slide-arrow{position:absolute;top:392px}

/* benefits */
.benefits{top:1820px;height:670px;color:var(--white)}
.benefits-photo{position:absolute;inset:0;background:linear-gradient(90deg,#f15a29 0%,#f26a38 50%,#d9623a 80%,#b4543a 100%)}
.benefits h2{position:absolute;left:147px;top:140px;font-size:38px;font-weight:700;line-height:52px}
.benefit-list{position:absolute;left:147px;top:274px;list-style:none;font-size:17px;font-weight:500}
.benefit-list li{display:flex;align-items:center;gap:18px;height:36px}

/* services */
.services{top:2490px;height:515px;text-align:center}
.services h2{font-size:38px;font-weight:700;line-height:52px;margin-top:88px}
.service-list{position:absolute;left:150px;top:250px;display:flex;list-style:none}
.service-list li{width:245px;font-size:17px;font-weight:500;color:#333;line-height:26px}
.service-list svg{display:block;margin:0 auto 14px}

/* markets */
.markets{top:3005px;height:495px}
.markets-head{height:180px;background:var(--orange);color:var(--white);text-align:center}
.markets-head h2{font-size:38px;font-weight:700;padding-top:58px}
.tiles{display:flex;height:315px;position:relative}
.tile{width:300px;height:315px;position:relative;display:flex;align-items:flex-end;justify-content:center;padding-bottom:40px;text-align:center;color:var(--white);font-size:17px;font-weight:700;line-height:26px;text-transform:uppercase}
.tile-insurance{background:linear-gradient(160deg,#8aa6c4,#3d5878)}
.tile-gov{background:linear-gradient(160deg,#10284c,#1e5a96)}
.tile-ecom{background:linear-gradient(160deg,#c9ccd0,#2e4a5a)}
.tile-commercial{background:linear-gradient(160deg,#e9e6e1,#5b4c44)}
.tile-arrow{position:absolute;top:130px;width:36px;height:56px;background:rgba(20,30,45,.75);display:flex;align-items:center;justify-content:center}

/* ebook */
.ebook{top:3500px;height:360px;text-align:center}
.ebook h2{font-size:38px;font-weight:700;margin-top:90px}
.ebook p{font-size:14px;color:var(--grey);line-height:27px;margin-top:14px}
.ebook-form{position:absolute;left:168px;top:280px;display:flex;gap:13px}
.field{width:310px;height:52px;border:1px solid var(--line);font-size:13px;color:#888;display:flex;align-items:center;padding-left:20px;text-align:left}
.ebook .btn{height:50px;width:216px;justify-content:center;font-size:16px;margin-left:2px}

/* footer */
.site-footer{top:3855px;height:422px}
.footer-brand{position:absolute;left:150px;top:222px;display:flex;align-items:center;gap:14px;color:var(--orange);font-family:'Catamaran',sans-serif;font-weight:700;font-size:64px;line-height:70px}
.footer-brand .brand-mark{width:20px;height:20px}
.address{position:absolute;left:533px;top:232px;display:flex;gap:18px;color:var(--white);font-size:14px;line-height:26px}
.pin{width:33px;height:33px;border-radius:50%;background:var(--white);display:flex;align-items:center;justify-content:center;margin-top:10px}
.social{position:absolute;left:858px;top:244px;display:flex;gap:7px;list-style:none}
.social li{width:33px;height:33px;border-radius:50%;background:var(--orange);display:flex;align-items:center;justify-content:center}
.legal{position:absolute;left:0;width:1200px;top:362px;text-align:center;color:var(--white);font-size:13px}
</style>
</head>
<body>

<header class="site-nav">
  <div class="brand"><span class="brand-mark"></span>Torvenda</div>
  <ul class="menu">
    <li class="active">HOME</li><li>MARKETS WE SERVE</li><li>INSIGHTS</li><li>CONTACT</li><li>APPLY TODAY</li>
  </ul>
  <div class="search"><svg width="35" height="35" viewBox="0 0 35 35"><circle cx="16" cy="16" r="4" fill="none" stroke="#fff" stroke-width="2"/><line x1="19" y1="19" x2="22" y2="22" stroke="#fff" stroke-width="2"/></svg></div>
</header>

<section class="hero">
  <div class="hero-photo" role="img" aria-label="Photo of hands typing on a laptop keyboard at an office desk"></div>
  <div class="hero-copy">
    <h1>GET MORE FROM YOUR<br>CUSTOMER INTERACTIONS</h1>
    <p>Lift Your Top and Bottom Lines with Professional<br>Outsourcing Solutions from Torvenda</p>
    <span class="btn">GET STARTED <svg width="16" height="16" viewBox="0 0 16 16"><circle cx="8" cy="8" r="8" fill="#fff"/><path d="M6 4.5 9.5 8 6 11.5" fill="none" stroke="#f15a29" stroke-width="2"/></svg></span>
  </div>
  <div class="dots"><span></span><span></span><span class="on"></span><span></span><span></span></div>
  <svg class="hero-cut" width="1200" height="110" viewBox="0 0 1200 110">
    <polygon points="0,110 0,105 720,40 1200,110" fill="#fff"/>
    <polygon points="720,40 1200,0 1200,95" fill="#f15a29"/>
    <polygon points="720,40 1200,95 1200,110 960,110" fill="#1f4a78"/>
  </svg>
</section>

<section class="intro">
  <h2>It’s a new world.are you ready?</h2>
  <p>It’s time to find solutions that deliver more value. Shed the manual interactions that cost you money and distract you from your core.<br>Get more by partnering with Torvenda for Customer Service, Tech Support, and Business Process Outsourcing solutions.</p>
</section>

<section class="strengths">
  <div class="strengths-photo" role="img" aria-label="Blue-toned photo of a team meeting around a conference table"></div>
  <h2>Better. Faster. Leaner. Smarter</h2>
  <p class="lede">Get More from Your Customer Interactions</p>
  <svg class="slide-arrow" style="left:72px" width="36" height="66" viewBox="0 0 36 66"><path d="M34 2 2 33l32 31" fill="none" stroke="rgba(255,255,255,.5)" stroke-width="2"/></svg>
  <svg class="slide-arrow" style="left:1092px" width="36" height="66" viewBox="0 0 36 66"><path d="M2 2l32 31L2 64" fill="none" stroke="rgba(255,255,255,.5)" stroke-width="2"/></svg>
  <ul class="pillars">
    <li><div class="ring"><div class="ring-inner"><svg width="70" height="70" viewBox="0 0 70 70" fill="none" stroke="#fff" stroke-width="2"><rect x="8" y="8" width="14" height="12"/><circle cx="56" cy="14" r="7"/><circle cx="35" cy="35" r="11"/><line x1="24" y1="35" x2="46" y2="35"/><circle cx="16" cy="54" r="6"/><circle cx="54" cy="50" r="6"/><path d="M44 66c0-8 20-8 20 0"/></svg></div></div>More Value</li>
    <li><div class="ring"><div class="ring-inner"><svg width="70" height="70" viewBox="0 0 70 70" fill="none" stroke="#fff" stroke-width="2"><rect x="6" y="12" width="58" height="38" rx="2"/><line x1="35" y1="50" x2="35" y2="60"/><line x1="22" y1="60" x2="48" y2="60"/><path d="M26 42l10-20 14-8-4 16-16 12z"/></svg></div></div>More<br>Performance</li>
    <li><div class="ring"><div class="ring-inner"><svg width="70" height="70" viewBox="0 0 70 70" fill="none" stroke="#fff" stroke-width="2"><circle cx="35" cy="35" r="22"/><circle cx="35" cy="35" r="6"/><line x1="35" y1="5" x2="35" y2="22"/><line x1="35" y1="48" x2="35" y2="65"/><line x1="5" y1="35" x2="22" y2="35"/><line x1="48" y1="35" x2="65" y2="35"/></svg></div></div>More Focus</li>
    <li><div class="ring"><div class="ring-inner"><svg width="70" height="70" viewBox="0 0 70 70" fill="none" stroke="#fff" stroke-width="2"><path d="M35 8l22 8v18c0 14-10 24-22 28-12-4-22-14-22-28V16z"/><path d="M26 36l7 7 12-14"/></svg></div></div>More Loyalty</li>
    <li><div class="ring"><div class="ring-inner"><svg width="70" height="70" viewBox="0 0 70 70" fill="none" stroke="#fff" stroke-width="2"><rect x="8" y="8" width="54" height="54"/><rect x="16" y="40" width="8" height="16"/><rect x="30" y="32" width="8" height="24"/><rect x="44" y="24" width="8" height="32"/><path d="M18 30l14-8 12 6 10-10"/></svg></div></div>More Insights</li>
  </ul>
</section>

<section class="benefits">
  <div class="benefits-photo" role="img" aria-label="Orange-toned photo of three colleagues smiling at a laptop"></div>
  <h2>Discover the Benefits<br>of Outsourcing</h2>
  <ul class="benefit-list">
    <li><svg width="16" height="16" viewBox="0 0 16 16"><circle cx="8" cy="8" r="7" fill="none" stroke="#fff" stroke-width="1.6"/><path d="M4.8 8.2l2.2 2.2 4-4.2" fill="none" stroke="#fff" stroke-width="1.6"/></svg>Shed overhead and invest in core resources.</li>
    <li><svg width="16" height="16" viewBox="0 0 16 16"><circle cx="8" cy="8" r="7" fill="none" stroke="#fff" stroke-width="1.6"/><path d="M4.8 8.2l2.2 2.2 4-4.2" fill="none" stroke="#fff" stroke-width="1.6"/></svg>Reduce risk – Lower headcount, infrastructure, and technology costs.</li>
    <li><svg width="16" height="16" viewBox="0 0 16 16"><circle cx="8" cy="8" r="7" fill="none" stroke="#fff" stroke-width="1.6"/><path d="M4.8 8.2l2.2 2.2 4-4.2" fill="none" stroke="#fff" stroke-width="1.6"/></svg>Scale up and down as needed.</li>
    <li><svg width="16" height="16" viewBox="0 0 16 16"><circle cx="8" cy="8" r="7" fill="none" stroke="#fff" stroke-width="1.6"/><path d="M4.8 8.2l2.2 2.2 4-4.2" fill="none" stroke="#fff" stroke-width="1.6"/></svg>Focus on your business, not on labor-intensive processes.</li>
    <li><svg width="16" height="16" viewBox="0 0 16 16"><circle cx="8" cy="8" r="7" fill="none" stroke="#fff" stroke-width="1.6"/><path d="M4.8 8.2l2.2 2.2 4-4.2" fill="none" stroke="#fff" stroke-width="1.6"/></svg>Build customer affinity with professional service teams.</li>
    <li><svg width="16" height="16" viewBox="0 0 16 16"><circle cx="8" cy="8" r="7" fill="none" stroke="#fff" stroke-width="1.6"/><path d="M4.8 8.2l2.2 2.2 4-4.2" fill="none" stroke="#fff" stroke-width="1.6"/></svg>Continuous improvement via performance management.</li>
    <li><svg width="16" height="16" viewBox="0 0 16 16"><circle cx="8" cy="8" r="7" fill="none" stroke="#fff" stroke-width="1.6"/><path d="M4.8 8.2l2.2 2.2 4-4.2" fill="none" stroke="#fff" stroke-width="1.6"/></svg>Access data to make better business decisions.</li>
  </ul>
</section>

<section class="services">
  <h2>Flexible, versatile, end-to-end outsourcing options<br>to help you get more of what your business needs.</h2>
  <ul class="service-list">
    <li><svg width="90" height="90" viewBox="0 0 90 90" fill="none" stroke="#1f4a78" stroke-width="2.5"><path d="M20 50V40a25 25 0 0 1 50 0v10"/><rect x="14" y="44" width="10" height="18" rx="4"/><rect x="66" y="44" width="10" height="18" rx="4"/><path d="M70 62c0 12-12 18-22 18"/><circle cx="46" cy="80" r="3" fill="#f15a29" stroke="none"/></svg>Customer Service<br>Contact Center</li>
    <li><svg width="90" height="90" viewBox="0 0 90 90" fill="none" stroke="#1f4a78" stroke-width="2.5"><circle cx="36" cy="28" r="14"/><path d="M12 78c0-18 12-26 24-26 6 0 10 2 13 4"/><circle cx="64" cy="64" r="12"/><circle cx="64" cy="64" r="5" stroke="#f15a29"/></svg>Tech Support<br>Service Center</li>
    <li><svg width="90" height="90" viewBox="0 0 90 90" fill="none" stroke="#1f4a78" stroke-width="2.5"><circle cx="20" cy="18" r="8"/><circle cx="70" cy="18" r="8"/><path d="M15 52a30 30 0 0 0 60 0"/><line x1="15" y1="52" x2="75" y2="52"/><rect x="36" y="34" width="18" height="18" stroke="#f15a29"/><line x1="45" y1="10" x2="45" y2="30"/></svg>Business Process<br>Outsourcing</li>
    <li><svg width="90" height="90" viewBox="0 0 90 90" fill="none" stroke="#1f4a78" stroke-width="2.5"><path d="M45 8l5 11 12 1-9 8 3 12-11-7-11 7 3-12-9-8 12-1z" stroke="#f15a29"/><path d="M38 48v32h22V58l-10-4V44"/><line x1="14" y1="22" x2="24" y2="26"/><line x1="76" y1="22" x2="66" y2="26"/></svg>End-to-End<br>Solutions</li>
  </ul>
</section>

<section class="markets">
  <div class="markets-head"><h2>We Serve Your Market</h2></div>
  <div class="tiles">
    <div class="tile tile-insurance" role="img" aria-label="Photo of a hand signing an insurance document">Insurance Contact<br>Center Services</div>
    <div class="tile tile-gov" role="img" aria-label="Photo of a hand touching a blue data screen">Government Contact<br>Center Solutions</div>
    <div class="tile tile-ecom" role="img" aria-label="Photo of a laptop showing an online shopping cart">Customer Service<br>for Ecommerce</div>
    <div class="tile tile-commercial" role="img" aria-label="Photo of a smiling business professional">Commercial Business<br>Customer Service &amp;<br>Tech Support</div>
    <div class="tile-arrow" style="left:0"><svg width="12" height="20" viewBox="0 0 12 20"><path d="M10 2 2 10l8 8" fill="none" stroke="#fff" stroke-width="2.5"/></svg></div>
    <div class="tile-arrow" style="left:1164px"><svg width="12" height="20" viewBox="0 0 12 20"><path d="M2 2l8 8-8 8" fill="none" stroke="#fff" stroke-width="2.5"/></svg></div>
  </div>
</section>

<section class="ebook">
  <h2>The Economics of Outsourcing</h2>
  <p>Take a hard look at your operating model. What overhead and labor costs can you shed? How can you<br>change in order to become more competitive? Our eBook shows you the way.</p>
  <div class="ebook-form">
    <div class="field">Enter name</div>
    <div class="field">Enter Email</div>
    <span class="btn">LINK TO EBOOK</span>
  </div>
</section>

<footer class="site-footer">
  <svg style="position:absolute;left:0;top:0" width="1200" height="422" viewBox="0 0 1200 422">
    <polygon points="0,0 1200,110 1200,422 0,422" fill="#1f4a78"/>
    <polygon points="0,70 345,175 0,175" fill="#f15a29"/>
    <polygon points="0,175 345,175 0,200" fill="#1f4a78"/>
  </svg>
  <div class="footer-brand"><span class="brand-mark"></span>Torvenda</div>
  <div class="address">
    <span class="pin"><svg width="14" height="18" viewBox="0 0 14 18"><path d="M7 17s6-6.5 6-10.5A6 6 0 0 0 1 6.5C1 10.5 7 17 7 17z" fill="#f15a29"/><circle cx="7" cy="6.5" r="2.2" fill="#fff"/></svg></span>
    <span>18 Harbor Lane, Unit 4, Suite 210<br>Castine, ME 04021</span>
  </div>
  <ul class="social">
    <li></li><li></li><li></li>
    <li><svg width="14" height="14" viewBox="0 0 14 14"><path d="M3 1l2.5 3-1.5 1.5c1 2 2.5 3.5 4.5 4.5L10 8.5l3 2.5-1.5 2C6 13 1 8 1 2.5z" fill="#fff"/></svg></li>
    <li></li>
  </ul>
  <p class="legal">Copyright © 2020 Torvenda LLC . All Rights reserved &nbsp;|&nbsp; Privacy Policy</p>
</footer>

</body>
</html>
```